Creative Graphic Designer needed to create fabulous wash cloths

We are an Interior design business and are releasing a range of wash cloths.
We would like some innovative designs to have screen printed on these cloths.
We will only be printing on one side.

The size of the cloth is 18 cm x 20 cm and the colour of the cloth is variable.

At this stage we have selected white, turquoise, orange and apple green as the base colours we require. (see attached)

1. The first design should portray 'used for washing up' and
2. the second 'used for wiping around'. Or just 'wiping only' sink only.

These can be in image format or a combination of image and text.

I am happy for you to use the whole of the cloth, or as little as you see fit.

I would see two print colours or max three, onto the base cloth.

I have also attached our company logo which I would like incorporated somewhere on the cloth, it can be as small or large as you like.
We are looking for something really creative.

Thanks so much!

Target Market(s)

Medium to high end

Industry/Entity Type

Graphic Designer

Requirements
Must have
• include the logo somewhere on the wash cloth. Final design must be in .eps or pdf. and KOLVENE colours.
Nice to have
• Something really fun and creative, however we are looking for originality
• I have included some concepts previously done to show what can be done.
• I dont mind if they are images, scenes, text, whatever you feel portrays the 'use for in the sink' and use for wiping around best.
• The attached image of New York I particularly like, I understand it has used alot more colours, but I found the concept really nice.
Should not have
• More than three colours.

```html
<!DOCTYPE html>
<html lang="en">
<head>
<meta charset="utf-8">
<title>Wash Cloth Range – Sink Only / Dish Only</title>
<link href="https://fonts.googleapis.com/css2?family=Bungee&display=swap" rel="stylesheet">
<style>
  :root {
    --cloth-white: #f8f7f0;
    --cloth-turquoise: #2db3bb;
    --cloth-orange: #f29a50;
    --cloth-green: #bcd672;
    --ink-dark: #474747;
    --ink-cream: #f8f7f0;
    --label-dark: #333333;
  }
  html, body {
    margin: 0;
    padding: 0;
    width: 1200px;
    height: 848px;
    overflow: hidden;
  }
  body {
    position: relative;
    background: radial-gradient(ellipse at 50% 45%, #ffffff 0%, #ececec 45%, #c6c6c6 100%);
    font-family: Arial, Helvetica, sans-serif;
  }
  .swatch, .cloth {
    position: absolute;
    width: 224px;
  }
  .swatch {
    top: 72px;
    height: 100px;
    display: flex;
    align-items: center;
    justify-content: center;
    font-weight: bold;
    font-style: italic;
    font-size: 20px;
    box-sizing: border-box;
  }
  .cloth { height: 249px; }
  .cloth svg { display: block; width: 224px; height: 249px; }
  .row-sink { top: 237px; }
  .row-dish { top: 526px; }
  .col-white { left: 60px; }
  .col-turquoise { left: 345px; }
  .col-orange { left: 630px; }
  .col-green { left: 917px; }

  .swatch.col-white { background: var(--cloth-white); border: 1px solid #d6d6d0; color: var(--label-dark); }
  .swatch.col-turquoise { background: var(--cloth-turquoise); color: var(--ink-cream); }
  .swatch.col-orange { background: var(--cloth-orange); color: var(--ink-cream); }
  .swatch.col-green { background: var(--cloth-green); color: var(--label-dark); }

  .cloth.col-white { background: var(--cloth-white); outline: 1px solid #d6d6d0; }
  .cloth.col-turquoise { background: var(--cloth-turquoise); }
  .cloth.col-orange { background: var(--cloth-orange); }
  .cloth.col-green { background: var(--cloth-green); }

  .word {
    font-family: "Bungee", "Arial Black", sans-serif;
    font-size: 66px;
  }
  .ink-dark { fill: var(--ink-dark); }
  .ink-cream { fill: var(--ink-cream); }
  .ink-turquoise { fill: var(--cloth-turquoise); }
  .ink-orange { fill: var(--cloth-orange); }
</style>
</head>
<body>

  <div class="swatch col-white">white</div>
  <div class="swatch col-turquoise">turquoise</div>
  <div class="swatch col-orange">orange</div>
  <div class="swatch col-green">apple green</div>

  <!-- Sink Only range -->
  <div class="cloth row-sink col-white">
    <svg viewBox="0 0 224 249">
      <defs><linearGradient id="sink-white" x1="0" y1="0" x2="0" y2="1"><stop offset="0" stop-color="#2db3bb"/><stop offset="1" stop-color="#474747"/></linearGradient></defs>
      <text class="word ink-dark" x="12" y="68" textLength="200" lengthAdjust="spacingAndGlyphs">SINK</text>
      <rect x="26" y="74" width="172" height="98" rx="4" fill="url(#sink-white)" role="img" aria-label="Illustration of a kitchen sink with taps and a drain pipe"/>
      <text class="word ink-turquoise" x="12" y="238" textLength="200" lengthAdjust="spacingAndGlyphs">ONLY</text>
    </svg>
  </div>
  <div class="cloth row-sink col-turquoise">
    <svg viewBox="0 0 224 249">
      <defs><linearGradient id="sink-turq" x1="0" y1="0" x2="0" y2="1"><stop offset="0" stop-color="#f8f7f0"/><stop offset="1" stop-color="#474747"/></linearGradient></defs>
      <text class="word ink-dark" x="12" y="68" textLength="200" lengthAdjust="spacingAndGlyphs">SINK</text>
      <rect x="26" y="74" width="172" height="98" rx="4" fill="url(#sink-turq)" role="img" aria-label="Illustration of a kitchen sink with taps and a drain pipe"/>
      <text class="word ink-cream" x="12" y="238" textLength="200" lengthAdjust="spacingAndGlyphs">ONLY</text>
    </svg>
  </div>
  <div class="cloth row-sink col-orange">
    <svg viewBox="0 0 224 249">
      <defs><linearGradient id="sink-orange" x1="0" y1="0" x2="0" y2="1"><stop offset="0" stop-color="#f8f7f0"/><stop offset="1" stop-color="#474747"/></linearGradient></defs>
      <text class="word ink-dark" x="12" y="68" textLength="200" lengthAdjust="spacingAndGlyphs">SINK</text>
      <rect x="26" y="74" width="172" height="98" rx="4" fill="url(#sink-orange)" role="img" aria-label="Illustration of a kitchen sink with taps and a drain pipe"/>
      <text class="word ink-cream" x="12" y="238" textLength="200" lengthAdjust="spacingAndGlyphs">ONLY</text>
    </svg>
  </div>
  <div class="cloth row-sink col-green">
    <svg viewBox="0 0 224 249">
      <defs><linearGradient id="sink-green" x1="0" y1="0" x2="0" y2="1"><stop offset="0" stop-color="#f8f7f0"/><stop offset="1" stop-color="#474747"/></linearGradient></defs>
      <text class="word ink-dark" x="12" y="68" textLength="200" lengthAdjust="spacingAndGlyphs">SINK</text>
      <rect x="26" y="74" width="172" height="98" rx="4" fill="url(#sink-green)" role="img" aria-label="Illustration of a kitchen sink with taps and a drain pipe"/>
      <text class="word ink-cream" x="12" y="238" textLength="200" lengthAdjust="spacingAndGlyphs">ONLY</text>
    </svg>
  </div>

  <!-- Dish Only range -->
  <div class="cloth row-dish col-white">
    <svg viewBox="0 0 224 249">
      <defs><linearGradient id="dish-white" x1="0" y1="0" x2="1" y2="0"><stop offset="0" stop-color="#f29a50"/><stop offset="1" stop-color="#474747"/></linearGradient></defs>
      <text class="word ink-orange" x="12" y="68" textLength="200" lengthAdjust="spacingAndGlyphs">DISH</text>
      <rect x="18" y="74" width="196" height="98" rx="4" fill="url(#dish-white)" role="img" aria-label="Illustration of a fork, a plate and a glass"/>
      <text class="word ink-dark" x="12" y="238" textLength="200" lengthAdjust="spacingAndGlyphs">ONLY</text>
    </svg>
  </div>
  <div class="cloth row-dish col-turquoise">
    <svg viewBox="0 0 224 249">
      <defs><linearGradient id="dish-turq" x1="0" y1="0" x2="1" y2="0"><stop offset="0" stop-color="#f8f7f0"/><stop offset="1" stop-color="#474747"/></linearGradient></defs>
      <text class="word ink-cream" x="12" y="68" textLength="200" lengthAdjust="spacingAndGlyphs">DISH</text>
      <rect x="18" y="74" width="196" height="98" rx="4" fill="url(#dish-turq)" role="img" aria-label="Illustration of a fork, a plate and a glass"/>
      <text class="word ink-dark" x="12" y="238" textLength="200" lengthAdjust="spacingAndGlyphs">ONLY</text>
    </svg>
  </div>
  <div class="cloth row-dish col-orange">
    <svg viewBox="0 0 224 249">
      <defs><linearGradient id="dish-orange" x1="0" y1="0" x2="1" y2="0"><stop offset="0" stop-color="#f8f7f0"/><stop offset="1" stop-color="#474747"/></linearGradient></defs>
      <text class="word ink-cream" x="12" y="68" textLength="200" lengthAdjust="spacingAndGlyphs">DISH</text>
      <rect x="18" y="74" width="196" height="98" rx="4" fill="url(#dish-orange)" role="img" aria-label="Illustration of a fork, a plate and a glass"/>
      <text class="word ink-dark" x="12" y="238" textLength="200" lengthAdjust="spacingAndGlyphs">ONLY</text>
    </svg>
  </div>
  <div class="cloth row-dish col-green">
    <svg viewBox="0 0 224 249">
      <defs><linearGradient id="dish-green" x1="0" y1="0" x2="1" y2="0"><stop offset="0" stop-color="#f8f7f0"/><stop offset="1" stop-color="#474747"/></linearGradient></defs>
      <text class="word ink-cream" x="12" y="68" textLength="200" lengthAdjust="spacingAndGlyphs">DISH</text>
      <rect x="18" y="74" width="196" height="98" rx="4" fill="url(#dish-green)" role="img" aria-label="Illustration of a fork, a plate and a glass"/>
      <text class="word ink-dark" x="12" y="238" textLength="200" lengthAdjust="spacingAndGlyphs">ONLY</text>
    </svg>
  </div>

</body>
</html>
```